Business Card Design Project

This is a new division in our company. "Kestrel Wellsite & Safety" This is a Oilfield Safety company. I have included our new logo. I also have given our other business card. We love double sided with lots of color. We like to stand out. Please DO NOT duplicate our other card and bring your design into it. See all attached files.
Reason: forgot to change this when I posted it.
Here is the correct information card.
www.kestrelwellsitesafety.example
Dwayne@kestrelwellsitesafety.example
Reason: revision for a few.
Reason: was traveling and need to review designs.
Target Market(s)
Oil and Gas industry. Masculine look.
Industry/Entity Type
Business
Look and feel

```html
<!DOCTYPE html>
<html lang="en">
<head>
<meta charset="utf-8">
<title>Kestrel Wellsite &amp; Safety – Business Cards</title>
<link rel="stylesheet" href="https://fonts.googleapis.com/css2?family=Lato:wght@400;700;900&display=swap">
<style>
  :root{
    --stage:#e9e6e1;
    --ink:#0a0a0a;
    --paper:#ffffff;
    --teal:#2bb8b2;
    --orange:#f04e23;
  }
  *{box-sizing:border-box;margin:0;padding:0}
  html,body{width:1200px;height:1000px;overflow:hidden}
  body{background:var(--stage);font-family:"Lato",sans-serif;position:relative}
  .card{position:absolute;left:250px;width:700px;height:400px;border-radius:18px;overflow:hidden;box-shadow:0 6px 18px rgba(0,0,0,.18)}
  .card--front{top:60px;background:var(--ink)}
  .card--back{top:540px;background:var(--paper)}

  .brand{display:flex;align-items:center;justify-content:center;gap:16px}
  .brand__mark{width:26px;height:26px;background:var(--orange)}
  .brand__name{font-weight:900;color:var(--teal);font-size:40px;letter-spacing:.5px;text-transform:uppercase}

  .card--front .brand{margin-top:118px}
  .tagline{text-align:center;color:var(--teal);font-weight:700;font-size:20px;margin-top:18px;text-transform:uppercase;letter-spacing:.5px}
  .website{position:absolute;left:0;right:0;top:305px;text-align:center;color:var(--orange);font-weight:700;font-size:20px;letter-spacing:.5px}

  .card--back .brand{margin-top:42px}
  .person{text-align:center;margin-top:46px}
  .person__name{color:var(--teal);font-weight:700;font-size:27px;letter-spacing:1px;text-transform:uppercase}
  .person__role{color:var(--orange);font-size:18px;margin-top:2px}
  .contact{list-style:none;text-align:center;margin-top:26px;color:var(--teal);font-size:19px;line-height:22px;letter-spacing:.4px}
  .contact__label{color:var(--orange);font-weight:700}

  .stripes{position:absolute;left:0;right:0;bottom:0;height:44px}
  .stripes__orange{position:absolute;left:0;right:0;top:0;height:8px;background:var(--orange)}
  .stripes__teal{position:absolute;left:0;right:0;bottom:0;height:26px;background:var(--teal)}
</style>
</head>
<body>
  <section class="card card--front">
    <div class="brand">
      <span class="brand__mark"></span>
      <span class="brand__name">Kestrel Wellsite &amp; Safety</span>
    </div>
    <p class="tagline">For all your oil &amp; gas equipment needs</p>
    <p class="website">www.kestrelwellsitesafety.example</p>
  </section>

  <section class="card card--back">
    <div class="brand">
      <span class="brand__mark"></span>
      <span class="brand__name">Kestrel Wellsite &amp; Safety</span>
    </div>
    <div class="person">
      <p class="person__name">Dwayne Harlan</p>
      <p class="person__role">Partner</p>
    </div>
    <ul class="contact">
      <li><span class="contact__label">P:</span> 555-201-4478</li>
      <li><span class="contact__label">F:</span> 1-800-555-0162</li>
      <li><span class="contact__label">M:</span> 555-309-6615</li>
      <li><span class="contact__label">E:</span> Dwayne@kestrelwellsitesafety.example</li>
      <li><span class="contact__label">A:</span> 4820 County Road 12, Redmesa, TX 75000</li>
    </ul>
    <div class="stripes">
      <div class="stripes__orange"></div>
      <div class="stripes__teal"></div>
    </div>
  </section>
</body>
</html>
```